Website Design for Business Law Firm

We have a logo and now we would like a web site design for our new website. Our small firm provides creative and aggressive transactional (not litigation) legal services to advise healthcare, technology, internet-based and traditional companies and investors in such companies on healthcare, technology, financing, mergers/acquisitions, real estate and other transactions, legal compliance and general corporate and business matters.

We would like to see a website design that is professional and appropriate for executives, professionals, investors and government regulators to visit, that conveys professionalism and competence while being a little edgy and modern - no typical legal motifs such as gavels, books, or scales of justice. We advise businesses and investors and guide them through complicated issues quickly, capably and differently from other law firms. We are part of the business team and get things done.

The logo is attached, and we like gray as a color to complement it. The intention of the logo is to convey that in a storm or challenging time, people come to this firm, and people come to this firm when they need the power and disruption to change things or shake them up.

I have also enclosed a picture of our business card for consideration.

On the other hand, you can check out the current simple site at www.venhollow.example to see we have used a space motif in the past to evoke that we help create stars (the nebula featured there). This is not a necessary part of the new website and it may look better without it.

We appreciate your creativity and look forward to designs.

Industry/Entity Type

Business

Requirements
Must have
• We anticipate the following pages, and you may submit different ideas for the different pages:
• 1. Landing page
• 2. Services pages - healthcare, IT/Technology, general counsel services, financings, mergers/acquisitions, mediation/arbitration, procurement and productization
• 3. About Us including contact information
• Our name and contact information:
• Quellane Law Firm, P.C.
• 8716 SW 19th Ave.
• Portland, OR 97213
• phone: 971.555.0143
• fax: 971.555.0187
Nice to have
• Please consider designs that enhance the impressions we are looking for
Should not have
• Please no gavels, scales of justice, law books, or similar traditional legal imagery.

```html
<!DOCTYPE html>
<html lang="en">
<head>
<meta charset="utf-8">
<title>Quellane Law Firm</title>
<link rel="stylesheet" href="https://fonts.googleapis.com/css2?family=Arimo:wght@400;700&family=Open+Sans:wght@400;600&family=Oswald:wght@400&display=swap">
<style>
:root{
  --charcoal:#3e424a;
  --charcoal-deep:#2e3138;
  --nav-top:#f3f6f9;
  --nav-bottom:#c8d2dc;
  --nav-divider:#aab4be;
  --ink:#2b2b2b;
  --ink-soft:#444;
  --paper:#ffffff;
  --footer-text:#c9ccd1;
  --button-top:#6f8794;
  --button-bottom:#3f5561;
  --tick:#2fa0d6;
  --rule:#d6d6d6;
}
*{margin:0;padding:0;box-sizing:border-box}
html,body{width:1031px;height:1200px;overflow:hidden}
body{position:relative;background:var(--charcoal);font-family:Arimo,Arial,sans-serif;color:var(--ink)}
.abs{position:absolute}

/* header */
.site-header{left:0;top:0;width:1031px;height:151px;background:var(--charcoal)}
.brand{left:72px;top:48px;height:64px;display:flex;align-items:center;gap:14px}
.brand-square{width:22px;height:22px;background:#7fa7a9}
.brand-name{font-family:"Open Sans",sans-serif;font-weight:400;font-size:40px;letter-spacing:9px;color:#e8ecee}
.contact-lines{left:808px;top:44px}
.contact-line{display:flex;align-items:center;gap:10px;height:31px;font-family:Oswald,sans-serif;font-size:24px;color:#f2f2f2}
.contact-line svg{width:18px;height:18px}

/* nav */
.main-nav{left:0;top:151px;width:1031px;height:45px;background:linear-gradient(var(--nav-top),var(--nav-bottom))}
.main-nav ul{list-style:none;display:flex;position:absolute;left:72px;top:0;height:45px}
.main-nav li{height:45px;line-height:45px;font-family:"Open Sans",sans-serif;font-size:18px;color:#3a3f45;border-right:1px solid var(--nav-divider);text-align:center}

/* hero */
.hero{left:0;top:196px;width:1031px;height:292px;background:linear-gradient(100deg,#c9d3dc 0%,#e6e4dc 30%,#d8cdbb 52%,#b08a6a 62%,#e5d6c8 74%,#dde2e8 90%,#c2ccd6 100%)}
.hero-arrow{width:40px;height:40px;background:#5c5f63}
.hero-caption{left:73px;top:400px;width:325px;height:88px;background:rgba(186,202,206,.88);padding:11px 12px;font-family:"Open Sans",sans-serif;font-size:22px;line-height:28px;color:#4a4f54}

/* content */
.content{left:0;top:488px;width:1031px;height:456px;background:var(--paper)}
.hero-shadow{left:80px;top:488px;width:870px;height:26px;background:radial-gradient(ellipse at 50% 0%,rgba(0,0,0,.35),rgba(0,0,0,0) 70%)}
.sector{width:253px;text-align:center}
.sector h2{font-family:"Open Sans",sans-serif;font-weight:400;font-size:18px;color:#222;margin-bottom:12px}
.sector p{text-align:left;font-size:12px;line-height:13.6px;color:#333}
.more-btn{display:block;width:84px;height:24px;line-height:24px;text-align:center;font-family:Arimo,sans-serif;font-weight:700;font-size:9px;color:#fff;background:linear-gradient(var(--button-top),var(--button-bottom));box-shadow:0 3px 5px rgba(0,0,0,.35)}
.sector .more-btn{margin:24px auto 0}
.divider{left:72px;top:706px;width:881px;height:1px;background:var(--rule)}
.welcome{left:73px;top:730px;width:632px}
.welcome h1,.features h2{font-family:"Open Sans",sans-serif;font-weight:400;font-size:22px;color:#222}
.welcome p{margin-top:8px;font-size:11.3px;line-height:12.4px;color:#333;text-align:justify}
.features{left:774px;top:726px;width:180px}
.features ul{list-style:none;margin-top:10px}
.features li{display:flex;align-items:center;gap:8px;height:24.5px;font-size:12px;color:#333}
.features li svg{width:12px;height:12px}

/* footer */
.site-footer{left:0;top:944px;width:1031px;height:218px;background:var(--charcoal)}
.footer-heading{font-size:18px;color:#f0f0f0;font-weight:400}
.quick-links{left:68px;top:962px;width:112px}
.quick-links ul{list-style:none;margin-top:10px}
.quick-links li{height:17px;line-height:16px;font-size:11px;color:var(--footer-text);border-bottom:1px solid #4f535b;padding-left:7px}
.mission{left:254px;top:962px;width:205px}
.footer-copy{margin-top:12px;font-size:10.5px;line-height:12.4px;color:var(--footer-text)}
.testimonials{left:523px;top:962px;width:215px}
.testimonials .footer-copy{padding-left:10px;position:relative}
.quote-mark{position:absolute;font-family:Georgia,serif;font-size:16px;color:var(--footer-text)}
.testimonial-author{margin-top:8px;text-align:center;font-size:12px;color:var(--footer-text);text-decoration:underline}
.follow{left:787px;top:962px}
.social{display:flex;gap:6px;margin-top:20px}
.social span{width:28px;height:28px;border-radius:50%;background:#8d9096}
.legal-bar{left:0;top:1162px;width:1031px;height:38px;background:var(--charcoal-deep);font-size:11px;color:var(--footer-text);line-height:38px}
.legal-bar .copyright{position:absolute;left:72px}
.legal-bar .legal-links{position:absolute;right:77px}
</style>
</head>
<body>

<header class="abs site-header">
  <div class="abs brand"><span class="brand-square"></span><span class="brand-name">QUELLANE</span></div>
  <div class="abs contact-lines">
    <div class="contact-line">
      <svg viewBox="0 0 24 24"><path fill="#f2f2f2" d="M6.6 10.8c1.4 2.8 3.8 5.1 6.6 6.6l2.2-2.2c.3-.3.7-.4 1-.2 1.1.4 2.3.6 3.6.6.6 0 1 .4 1 1V20c0 .6-.4 1-1 1C10.6 21 3 13.4 3 4c0-.6.4-1 1-1h3.5c.6 0 1 .4 1 1 0 1.3.2 2.5.6 3.6.1.3 0 .7-.2 1z"/></svg>
      <span>971.555.0143</span>
    </div>
    <div class="contact-line">
      <svg viewBox="0 0 24 24"><path fill="#f2f2f2" d="M6 2h12v6H6zM3 9h18a1 1 0 0 1 1 1v7h-4v5H6v-5H2v-7a1 1 0 0 1 1-1zm5 6v5h8v-5z"/></svg>
      <span>971.555.0187</span>
    </div>
  </div>
</header>

<nav class="abs main-nav">
  <ul>
    <li style="width:73px">Home</li>
    <li style="width:114px">About Us</li>
    <li style="width:107px">Services</li>
    <li style="width:114px">Expertise</li>
    <li style="width:91px">Client</li>
    <li style="width:77px">Blog</li>
    <li style="width:104px">Careers</li>
    <li style="width:123px">Contact Us</li>
  </ul>
</nav>

<section class="abs hero" role="img" aria-label="Photo of a hand holding a small model house in front of a blurred building and sky"></section>
<div class="abs hero-arrow" style="left:31px;top:337px"><svg viewBox="0 0 40 40" width="40" height="40"><path d="M24 11 15 20l9 9" fill="none" stroke="#fff" stroke-width="4"/></svg></div>
<div class="abs hero-arrow" style="left:953px;top:337px"><svg viewBox="0 0 40 40" width="40" height="40"><path d="M16 11l9 9-9 9" fill="none" stroke="#fff" stroke-width="4"/></svg></div>
<div class="abs hero-caption">Pragmatic, Creative Services<br>for Innovative Businesses</div>

<main class="abs content"></main>
<div class="abs hero-shadow"></div>

<section class="abs sector" style="left:77px;top:525px">
  <h2>Healthcare</h2>
  <p>Lorem ipsum dolor sit amet, consectetur adip-isicing elit, sed do eiusmod tempor incididunt ut labore et dolore magna aliqua. Ut enim ad minim veniam, quis nostrud exercitation ullam-co laboris nisi ut aliquip ex ea commodo</p>
  <span class="more-btn">Know More</span>
</section>
<section class="abs sector" style="left:389px;top:525px">
  <h2>Real Estate</h2>
  <p>Lorem ipsum dolor sit amet, consectetur adip-isicing elit, sed do eiusmod tempor incididunt ut labore et dolore magna aliqua. Ut enim ad minim veniam, quis nostrud exercitation ullam-co laboris nisi ut aliquip ex ea commodo</p>
  <span class="more-btn">Know More</span>
</section>
<section class="abs sector" style="left:690px;top:525px">
  <h2>Financing</h2>
  <p>Lorem ipsum dolor sit amet, consectetur adip-isicing elit, sed do eiusmod tempor incididunt ut labore et dolore magna aliqua. Ut enim ad minim veniam, quis nostrud exercitation ullam-co laboris nisi ut aliquip ex ea commodo</p>
  <span class="more-btn">Know More</span>
</section>

<div class="abs divider"></div>

<section class="abs welcome">
  <h1>Welcome to Quellane</h1>
  <p>Lorem ipsum dolor sit amet, consectetur adipiscing elit. Curabitur in tortor nisl. Curabitur pharetra, ante et semper placerat, mauris tortor ullamcorper libero, quis fringilla tellus nulla eget arcuLorem ipsum dolor sit amet, consectetur adipiscing elit. Lorem ipsum dolor sit amet, consectetur adipiscing elit. Curabitur in tortor nisl. Curabitur pharetra, ante et semper placerat, mauris tortor ullamcorper libero, quis fringilla tellus nulla eget arcuLorem ipsum dolor sit amet, consectetur adipiscing elit. Lorem ipsum dolor sit amet, consectetur adipiscing elit. Curabitur in tortor nisl. Curabitur pharetra, ante et semper placerat, mauris tortor ullamcorper libero, quis fringilla tellus nulla eget arcuLorem ipsum dolor sit amet, consectetur adipiscing elit. Lorem ipsum dolor sit amet, consectetur adipiscing elit.</p>
  <span class="more-btn" style="margin-top:28px">Know More</span>
</section>

<section class="abs features">
  <h2>Features</h2>
  <ul>
    <li><svg viewBox="0 0 12 12"><path d="M1 6.5 4.5 10 11 2" fill="none" stroke="var(--tick)" stroke-width="2.4"/></svg>Strategic Alliances</li>
    <li><svg viewBox="0 0 12 12"><path d="M1 6.5 4.5 10 11 2" fill="none" stroke="var(--tick)" stroke-width="2.4"/></svg>Business Relationships</li>
    <li><svg viewBox="0 0 12 12"><path d="M1 6.5 4.5 10 11 2" fill="none" stroke="var(--tick)" stroke-width="2.4"/></svg>Real Estate</li>
    <li><svg viewBox="0 0 12 12"><path d="M1 6.5 4.5 10 11 2" fill="none" stroke="var(--tick)" stroke-width="2.4"/></svg>Contracts</li>
    <li><svg viewBox="0 0 12 12"><path d="M1 6.5 4.5 10 11 2" fill="none" stroke="var(--tick)" stroke-width="2.4"/></svg>Vendor management</li>
  </ul>
  <span class="more-btn" style="margin-top:14px;margin-left:2px">Know More</span>
</section>

<footer class="abs site-footer"></footer>
<section class="abs quick-links">
  <h3 class="footer-heading">Quick Links</h3>
  <ul><li>Home</li><li>About Us</li><li>Services</li><li>Expertise</li><li>Client</li><li>Blog</li><li>Careers</li><li>Contact Us</li></ul>
</section>
<section class="abs mission">
  <h3 class="footer-heading">Our Mission</h3>
  <p class="footer-copy">Lorem ipsum dolor sit amet, consectetur adipiscing elit. Curabitur in tortor nisl. Curabitur pharetra, ante et semper plac-erat, mauris tortor ullamcorper libero, quis fringilla tellus nulla eget arcuLorem ipsum dolor sit amet, consectetur adipi-scing elit.</p>
</section>
<section class="abs testimonials">
  <h3 class="footer-heading">Testimonials</h3>
  <p class="footer-copy"><span class="quote-mark" style="left:-2px;top:-4px">&ldquo;</span>Lorem ipsum dolor sit amet, consectetur adipiscing elit. Curabitur in tortor nisl. Curabitur pharetra, ante et semper plac-erat, mauris tortor ullamcorper libero, quis fringilla tellus nulla eget arcuLorem ipsum dolor sit amet, consectetur adipi-scing elit.</p>
  <p class="testimonial-author">- LOREM IPSUM DOLOR <span style="text-decoration:none;font-family:Georgia,serif;font-size:15px">&rdquo;</span></p>
</section>
<section class="abs follow">
  <h3 class="footer-heading">Follow us on</h3>
  <div class="social"><span></span><span></span><span></span><span></span></div>
</section>

<div class="abs legal-bar">
  <span class="copyright">&copy; Copyright 2013 &nbsp;- All rights reserved.</span>
  <span class="legal-links">Copyright &nbsp;| &nbsp;Privacy Policy &nbsp;| &nbsp;Terms &nbsp;| &nbsp;Sitemap</span>
</div>

</body>
</html>
```